Large Bookmark Design for Visual Artist JR Holt

Design and complete a large bookmark page that acts as a brochure for a visual artist. This will replace the current trifold brochure and be 8.5 long by 3.66 in wide (an 8.5 in x 11 in page cut into 3). Files to be editable and printable on a standard colour printer.
We don't want another tri fold brochure - just a double sided large bookmark
The design will take the text and info from the existing brochure, simplify it and present it in a compelling way that will create interest. DOUBLE SIDED.

Target Market(s)

Art Collectors

Industry/Entity Type

Visual Arts

Font styles to use
Sans Serif

Colors
0054AA
0677BA
7BADD7
CADEEF
E8F1F8
00AB8E
00BBA5
67D7C9
C6EFE9
E9F9F6

Requirements
Must have
• Include the logo and a couple of artwork photos and website domain name
Nice to have
• simple, not too much text - this is a teaser product to generate website visits
Should not have
• too much information

```html
<!DOCTYPE html>
<html lang="en">
<head>
<meta charset="utf-8">
<title>JR Holt – Bookmark</title>
<link rel="stylesheet" href="https://fonts.googleapis.com/css2?family=Josefin+Sans:wght@600;700&family=Open+Sans:ital,wght@0,400;0,600;0,700;1,600;1,700&display=swap">
<style>
  :root {
    --backdrop: #525e6b;
    --paper: #ffffff;
    --ink: #2b3a4f;
    --body: #333a42;
    --mist: #e5e7ef;
    --accent-blue: #5b82c4;
    --accent-green: #2e7a66;
    --rule: #3a4350;
  }
  * { box-sizing: border-box; margin: 0; padding: 0; }
  html, body { width: 1200px; height: 1200px; overflow: hidden; background: var(--backdrop); }
  body { position: relative; font-family: "Open Sans", Arial, sans-serif; color: var(--body); }

  .bookmark {
    position: absolute; top: 90px; width: 439px; height: 1020px; background: var(--paper); overflow: hidden;
  }
  .bookmark--front { left: 119px; }
  .bookmark--back { left: 643px; }
  .bookmark > * { position: absolute; }

  .mist-block { background: var(--mist); }
  .tab-blue { background: var(--accent-blue); }
  .tab-green { background: var(--accent-green); }

  .artwork { display: block; }

  .headline {
    font-family: "Josefin Sans", Arial, sans-serif; font-weight: 600; color: var(--ink);
    letter-spacing: 0.5px; text-transform: uppercase;
  }
  .statement-title { left: 35px; top: 264px; font-size: 54px; line-height: 0.92; }
  .statement-body { left: 35px; top: 376px; width: 371px; font-size: 12.4px; line-height: 1.45; text-align: justify; }
  .statement-body p + p { margin-top: 15px; }
  .statement-body .lead { font-weight: 700; color: var(--ink); }

  .rule { left: 29px; width: 382px; height: 2px; background: var(--rule); }

  .brand { left: 0; width: 100%; top: 862px; display: flex; justify-content: center; align-items: center; gap: 14px; }
  .brand-dot { width: 40px; height: 40px; border-radius: 50%; background: var(--accent-blue); }
  .brand-text { display: flex; flex-direction: column; }
  .brand-name { font-family: "Open Sans", Arial, sans-serif; font-weight: 600; font-size: 38px; line-height: 1; color: var(--accent-blue); }
  .brand-tagline { font-style: italic; font-size: 12px; color: var(--accent-green); margin-top: 4px; text-align: right; }

  .site-url { right: 35px; top: 968px; font-weight: 700; font-size: 23px; color: var(--ink); letter-spacing: 0.3px; }

  .background-title { left: 35px; top: 36px; font-size: 30px; }
  .background-body { left: 35px; top: 86px; width: 371px; font-size: 12.4px; line-height: 1.4; text-align: justify; }
  .background-body p + p { margin-top: 17px; }

  .quote { left: 35px; top: 642px; width: 380px; font-style: italic; font-weight: 600; font-size: 19.5px; line-height: 1.22; color: var(--ink); }
  .quote-author { left: 35px; top: 764px; font-style: italic; font-weight: 700; font-size: 19px; color: var(--accent-blue); }

  .gallery-label { left: 35px; top: 842px; font-size: 20px; }
  .gallery-name { left: 35px; top: 884px; font-size: 27px; line-height: 1.02; }
  .gallery-contact { right: 35px; top: 882px; text-align: right; font-weight: 600; font-size: 16px; line-height: 1.2; color: var(--ink); }
</style>
</head>
<body>

  <section class="bookmark bookmark--front" aria-label="Artist's statement side">
    <div class="mist-block" style="left:0;top:0;width:290px;height:332px;"></div>
    <svg class="artwork" style="left:0;top:37px;" width="404" height="248" role="img" aria-label="Painting of caribou in a snowy winter forest at sunset">
      <defs>
        <linearGradient id="winter-glow" x1="0" y1="0" x2="0" y2="1">
          <stop offset="0" stop-color="#b69bc4"/>
          <stop offset="0.3" stop-color="#f2a77e"/>
          <stop offset="0.45" stop-color="#f7cf8e"/>
          <stop offset="0.6" stop-color="#8a8fb8"/>
          <stop offset="1" stop-color="#ece6ef"/>
        </linearGradient>
      </defs>
      <rect width="404" height="248" fill="url(#winter-glow)"/>
    </svg>
    <div class="tab-blue" style="left:0;top:26px;width:38px;height:22px;"></div>
    <div class="tab-green" style="left:394px;top:56px;width:23px;height:76px;"></div>

    <h1 class="headline statement-title">Artist’s<br>Statement</h1>

    <div class="statement-body">
      <p class="lead">As an Artist I seek to create an emotional response to the images I create. My work is representational and therefore the choice of subject is always an important consideration. In order to make the subject “speak” to the viewer in a spiritual way, however, there is much more involved.</p>
      <p>The artistic challenge for me is in combining form, colour, composition and subject in a way that makes it all work seamlessly. I strive to blend a number of elusive elements in just the right proportions and combine these to create an image on canvas.</p>
      <p>I use my technical skill as a tool to serve my artistic vision. My chosen medium is acrylic paint on canvas and my message reflects both the positive and challenging aspects of the human condition. I use art work as a means of telling a compelling story.</p>
      <p>I paint with bright, bold colours that are applied in “bricks” – each brick integrates with other bricks to form an overall seamless recognizable image. It’s a technique I describe as “Blockism™”.</p>
    </div>

    <div class="rule" style="top:830px;"></div>
    <div class="brand">
      <span class="brand-dot"></span>
      <div class="brand-text">
        <span class="brand-name">JR Holt</span>
        <span class="brand-tagline">Painter of Special Moments</span>
      </div>
    </div>
    <div class="rule" style="top:950px;"></div>
    <p class="site-url">www.jrholt.com</p>
  </section>

  <section class="bookmark bookmark--back" aria-label="Background side">
    <h2 class="headline background-title">Background</h2>
    <div class="background-body">
      <p>Born in Montreal, Quebec. She graduated from the Harbourview Academy of Fine Arts where she was taught and mentored by Walter Brandt, a founder of Canada’s “Northern Circle”</p>
      <p>She was awarded a Senior Certificate in Painting from the Prairie State University and studied at the Ridgeline School of Fine Arts as a scholarship student.</p>
    </div>

    <div class="mist-block" style="left:86px;top:265px;width:353px;height:347px;"></div>
    <svg class="artwork" style="left:35px;top:294px;" width="372" height="290" role="img" aria-label="Painting of a red rowboat in a harbour with colourful houses at sunset">
      <defs>
        <linearGradient id="harbour-glow" x1="0" y1="0" x2="0" y2="1">
          <stop offset="0" stop-color="#f4a24a"/>
          <stop offset="0.22" stop-color="#f7c46a"/>
          <stop offset="0.38" stop-color="#8bb65a"/>
          <stop offset="0.48" stop-color="#6fa0d6"/>
          <stop offset="1" stop-color="#3f74c2"/>
        </linearGradient>
      </defs>
      <rect width="372" height="290" fill="url(#harbour-glow)"/>
    </svg>
    <div class="tab-blue" style="left:400px;top:283px;width:39px;height:22px;"></div>
    <div class="tab-green" style="left:23px;top:456px;width:24px;height:76px;"></div>

    <p class="quote">“As an Artist, I have the opportunity to touch another person’s spirit. When my work makes that connection, it’s a truly special moment for me.”</p>
    <p class="quote-author">Jane R. Holt</p>

    <div class="rule" style="top:830px;"></div>
    <h3 class="headline gallery-label">Gallery</h3>
    <div class="rule" style="top:868px;"></div>
    <p class="headline gallery-name">Stone and<br>Tide</p>
    <p class="gallery-contact">218 Shoreline Road,<br>Harbour Bay BC<br>604-555-0142</p>
    <div class="rule" style="top:950px;"></div>
    <p class="site-url">www.jrholt.com</p>
  </section>

</body>
</html>
```